high-impact, conversion-focused website redesign for the government sector

Objective: To design and develop a high-impact, conversion-focused digital platform that solidifies Harrowfield Bright Associates (HBA) as the leading communications and strategy firm for government, defense, and industrial clients. The site must project authority, innovation, and sophisticated precision. See the creative breif for more information

Target Market(s)

Government contractors

Industry/Entity Type

Government, defense, industrials

Coding

Coded - Design and coding required

Number of Pages Required

5+ page

Font styles to use
Other font styles liked:
• See the current website

Requirements
Must have
• See design brief
Nice to have
• See design brief
Should not have
• See design brief

```html
<!DOCTYPE html>
<html lang="en">
<head>
<meta charset="utf-8">
<title>Harrowfield Bright Associates</title>
<link href="https://fonts.googleapis.com/css2?family=Exo+2:wght@300;400;600;700;800&family=Open+Sans:wght@400;600;700&display=swap" rel="stylesheet">
<style>
:root{
  --navy:#0b1a2b;
  --navy-deep:#07121f;
  --blue:#2b8fe0;
  --blue-light:#3fa9f5;
  --orange:#f05a24;
  --green:#7cc242;
  --yellow:#f6b31b;
  --teal:#2bb3a6;
  --white:#ffffff;
  --ink:#1c2530;
  --grey:#5b6570;
  --line:rgba(255,255,255,.25);
}
*{box-sizing:border-box;margin:0;padding:0}
html,body{width:1200px;height:4884px;overflow:hidden}
body{font-family:"Open Sans",Arial,sans-serif;color:var(--ink);background:var(--white);position:relative}
.head{font-family:"Exo 2",Arial,sans-serif;text-transform:uppercase}
section,footer{position:absolute;left:0;width:1200px;overflow:hidden}

/* hero */
.hero{top:0;height:1080px;background:var(--navy-deep)}
.hero-photo{position:absolute;inset:0;background:linear-gradient(180deg,#2e4a63 0%,#1b3145 28%,#0d1d2e 55%,#081421 100%)}
.nav{position:absolute;top:30px;left:0;width:1200px;display:flex;justify-content:center;align-items:center;gap:34px;color:var(--white);font-size:13px;font-weight:600}
.nav .active{color:var(--blue-light);display:flex;align-items:center;gap:8px}
.nav .active::before{content:"";width:8px;height:8px;background:var(--blue-light);border-radius:50%}
.brand{display:flex;align-items:center;gap:8px;margin:0 30px;font-family:"Exo 2",sans-serif;font-weight:700;font-size:17px;letter-spacing:1px;color:var(--white);text-transform:uppercase}
.brand i{width:14px;height:14px;background:var(--blue-light);border-radius:50%}
.hero-title{position:absolute;left:90px;top:460px;font-size:46px;font-weight:800;line-height:1.05;color:var(--white)}
.hero-title span{color:transparent;-webkit-text-stroke:1.5px var(--blue-light);font-size:58px;letter-spacing:2px}
.hero-title .dot{position:absolute;left:-4px;top:12px;width:18px;height:18px}
.hero-title .l1{padding-left:22px}
.hero-copy{position:absolute;left:620px;top:452px;width:430px;color:#d4dde6;font-size:12px;line-height:1.65}
.read-more{position:absolute;left:620px;top:580px;color:var(--white);font-size:11px;font-weight:700;display:flex;align-items:center;gap:10px}
.read-more b{width:26px;height:26px;border:1px solid var(--blue-light);border-radius:50%;display:flex;align-items:center;justify-content:center;color:var(--blue-light);font-size:12px}
.services-title{position:absolute;top:690px;width:100%;text-align:center;color:var(--white);font-size:44px;font-weight:600;letter-spacing:2px}
.view-all{position:absolute;top:706px;left:950px;font-size:11px;color:#c9d3dc;font-weight:600;display:flex;gap:10px;align-items:center}
.view-all b{width:22px;height:22px;border:1px solid #c9d3dc;border-radius:50%;display:flex;align-items:center;justify-content:center;font-size:10px}
.services{position:absolute;top:780px;left:0;width:1200px;display:flex;justify-content:center;gap:26px}
.service{position:relative;width:200px;height:200px;color:var(--white);text-align:center}
.service svg{position:absolute;inset:0}
.service p{position:absolute;top:122px;width:100%;font-family:"Exo 2",sans-serif;font-weight:700;font-size:13px;line-height:1.2;text-transform:uppercase}

/* partnering intro */
.intro{top:1080px;height:640px;background:var(--white)}
.intro-visual{position:absolute;left:180px;top:130px;width:380px;height:340px;background:linear-gradient(135deg,#2b8fe0 0%,#3a4a5a 45%,#f05a24 75%,#7cc242 100%)}
.intro-copy{position:absolute;left:640px;top:200px;width:380px;font-size:12.5px;line-height:1.75;color:var(--ink)}
.intro-copy ul{list-style:none;margin-top:14px}
.intro-copy li{font-weight:700;padding-left:14px;position:relative;line-height:1.8}
.intro-copy li::before{content:"";position:absolute;left:0;top:9px;width:6px;height:6px;background:var(--orange)}

/* growth */
.growth{top:1720px;height:680px;background:linear-gradient(180deg,#0d2136,#0a1828 60%,#0b1a2b)}
.eyebrow{display:flex;align-items:center;gap:10px;font-weight:700;font-size:14px;letter-spacing:1px}
.growth .eyebrow{position:absolute;left:90px;top:130px;color:var(--white)}
.growth h2{position:absolute;left:90px;top:152px;color:var(--white);font-weight:700;font-size:62px;letter-spacing:3px}
.growth .lead{position:absolute;left:90px;top:240px;width:720px;color:#c8d2dc;font-size:12px;line-height:1.6}
.stat{position:absolute;top:350px;color:var(--white)}
.stat strong{display:block;font-family:"Exo 2",sans-serif;font-weight:700;font-size:52px;color:var(--blue-light);line-height:1}
.stat p{font-size:11px;line-height:1.5;color:#c8d2dc;margin-top:8px;width:210px}
.stat-hex{position:absolute;left:780px;top:300px;width:200px;height:180px}
.stat-hex p{position:absolute;left:44px;top:78px;width:130px;font-size:10.5px;line-height:1.45;color:#e1e8ef}

/* testimonial */
.testimonial{top:2400px;height:560px;background:var(--white)}
.quote-mark{position:absolute;left:180px;top:100px}
.quote{position:absolute;left:180px;top:170px;width:390px;font-size:12px;line-height:1.75;color:var(--grey)}
.quote-name{position:absolute;left:180px;top:350px;font-family:"Exo 2",sans-serif;font-weight:700;font-size:24px;color:var(--ink)}
.quote-role{position:absolute;left:180px;top:382px;font-size:11px;color:var(--grey)}
.quote-nav{position:absolute;left:180px;top:408px}
.portrait{position:absolute;left:660px;top:50px;width:340px;height:392px;background:linear-gradient(160deg,#d5dbe0,#9aa6b1);clip-path:polygon(50% 0,100% 25%,100% 75%,50% 100%,0 75%,0 25%)}

/* edge */
.edge{top:2960px;height:720px}
.edge-photo{position:absolute;inset:0;background:linear-gradient(180deg,#5d6d7a 0%,#8a5a3e 20%,#4f6b80 45%,#1f6fae 75%,#1a64ad 100%)}
.edge h2{position:absolute;left:90px;top:505px;color:var(--white);font-weight:700;font-size:64px;letter-spacing:3px}
.edge p{position:absolute;left:90px;top:590px;width:760px;color:#e6eef6;font-size:12px;line-height:1.65}

/* partnering with us */
.partner{top:3680px;height:800px;background:var(--white)}
.partner .eyebrow{position:absolute;top:110px;left:0;width:100%;justify-content:center;color:var(--ink);font-size:12px}
.partner h2{position:absolute;top:132px;width:100%;text-align:center;font-weight:600;font-size:46px;letter-spacing:2px;color:var(--ink)}
.partner .lead{position:absolute;top:210px;left:200px;width:800px;text-align:center;font-size:12px;line-height:1.65;color:var(--grey)}
.wheel{position:absolute;left:190px;top:330px;width:400px;height:400px;border-radius:50%;background:radial-gradient(circle,#0b1a2b 0%,#2b8fe0 45%,#7cc242 75%,#f6b31b 100%)}
.partner-copy{position:absolute;left:640px;top:420px;width:370px;font-size:12px;line-height:1.7;color:var(--grey)}
.partner-copy p+p{margin-top:14px}
.btn{display:inline-block;margin-top:20px;background:var(--green);color:var(--white);font-weight:700;font-size:11px;padding:11px 22px;letter-spacing:.5px}

/* footer */
.footer{top:4480px;height:404px;background:linear-gradient(120deg,#0f2236 0%,#07121f 55%)}
.subscribe{position:absolute;left:100px;top:94px;color:var(--orange);font-weight:700;font-size:26px;line-height:1.05;letter-spacing:1px}
.subscribe span{color:var(--white);display:block}
.email-field{position:absolute;left:100px;top:200px;width:380px;border-bottom:1px solid var(--line);padding-bottom:10px;color:#9fb0c0;font-size:12px;display:flex;justify-content:space-between}
.foot-col{position:absolute;top:94px;color:#c8d2dc;font-size:12px;line-height:2}
.foot-col h4{font-family:"Exo 2",sans-serif;font-weight:700;text-transform:uppercase;color:var(--green);font-size:16px;letter-spacing:1px;margin-bottom:8px}
.foot-col.contact h4{color:var(--blue-light)}
.foot-col.contact div{line-height:1.6}
.contact-row{display:flex;gap:10px;align-items:flex-start;margin-bottom:6px}
.contact-row i{width:10px;height:10px;background:var(--blue-light);border-radius:50%;margin-top:4px;flex:none}
.copyright{position:absolute;bottom:24px;width:100%;text-align:center;color:#8193a4;font-size:10px;letter-spacing:1px;border-top:1px solid rgba(255,255,255,.08);padding-top:20px}
</style>
</head>
<body>

<section class="hero">
  <div class="hero-photo" role="img" aria-label="Aerial photograph of an aircraft carrier at sea, fading into dark navy"></div>
  <nav class="nav">
    <span class="active">Advisory Services</span>
    <span>About Us</span>
    <span class="brand"><i></i>Harrowfield Bright</span>
    <span>Blog</span>
    <span>Contact Us</span>
  </nav>
  <h1 class="hero-title head">
    <svg class="dot" viewBox="0 0 20 20"><polygon points="10,1 18,5.5 18,14.5 10,19 2,14.5 2,5.5" fill="#2b8fe0"/></svg>
    <div class="l1">Accelerate your</div>
    <span>Mission</span>
  </h1>
  <p class="hero-copy">Harrowfield Bright Associates exists for one reason: to help connect the federal ecosystem with the technologies that matter most to America and her allies. We help build the communications, government affairs and marketing strategies and systems your organization needs to grow and protect market share. Helping our clients meet their mission objectives.</p>
  <div class="read-more"><b>&#8250;</b>READ MORE</div>

  <h2 class="services-title head">Our Services</h2>
  <div class="view-all"><b>&#8250;</b>VIEW ALL SERVICES</div>

  <div class="services">
    <div class="service">
      <svg viewBox="0 0 200 200"><polygon points="100,4 186,52 186,148 100,196 14,148 14,52" fill="none" stroke="rgba(255,255,255,.35)" stroke-width="1.5"/><polygon points="100,36 134,55 134,93 100,112 66,93 66,55" fill="#f05a24"/><rect x="86" y="62" width="28" height="24" fill="none" stroke="#fff" stroke-width="2.5"/><line x1="82" y1="90" x2="118" y2="90" stroke="#fff" stroke-width="2.5"/></svg>
      <p>Government<br>Affairs</p>
    </div>
    <div class="service">
      <svg viewBox="0 0 200 200"><polygon points="100,4 186,52 186,148 100,196 14,148 14,52" fill="none" stroke="rgba(255,255,255,.35)" stroke-width="1.5"/><polygon points="100,36 134,55 134,93 100,112 66,93 66,55" fill="#2b8fe0"/><path d="M84 64h32v18h-18l-8 7v-7h-6z" fill="none" stroke="#fff" stroke-width="2.5"/></svg>
      <p>Crisis<br>Communications</p>
    </div>
    <div class="service">
      <svg viewBox="0 0 200 200"><polygon points="100,4 186,52 186,148 100,196 14,148 14,52" fill="none" stroke="rgba(255,255,255,.35)" stroke-width="1.5"/><polygon points="100,36 134,55 134,93 100,112 66,93 66,55" fill="#7cc242"/><polyline points="84,86 94,74 102,80 116,64" fill="none" stroke="#fff" stroke-width="2.5"/></svg>
      <p>Investor<br>Relations</p>
    </div>
    <div class="service">
      <svg viewBox="0 0 200 200"><polygon points="100,4 186,52 186,148 100,196 14,148 14,52" fill="none" stroke="rgba(255,255,255,.35)" stroke-width="1.5"/><polygon points="100,36 134,55 134,93 100,112 66,93 66,55" fill="#3fa9f5"/><rect x="84" y="62" width="32" height="22" rx="2" fill="none" stroke="#fff" stroke-width="2.5"/><line x1="92" y1="90" x2="108" y2="90" stroke="#fff" stroke-width="2.5"/></svg>
      <p>Digital<br>Marketing</p>
    </div>
  </div>
</section>

<section class="intro">
  <div class="intro-visual" role="img" aria-label="Collage of defense and industry photos set in coloured triangles"></div>
  <div class="intro-copy">
    <p>Partnering with Harrowfield Bright Associates accelerated the growth of our company. Their strategic insight, deep federal expertise, and hands-on support transformed our U.S. expansion. In less than six months, they built our presence in the United States from the ground up, helping us secure contracts, advocates, and visibility at the highest levels. Working with Harrowfield Bright Associates has been a true game changer for our company.</p>
    <ul>
      <li>Martin Calloway</li>
      <li>President &amp; Managing Director</li>
      <li>Ironvale Metals USA</li>
    </ul>
  </div>
</section>

<section class="growth">
  <div class="eyebrow head"><svg width="18" height="18" viewBox="0 0 20 20"><polygon points="10,1 18,5.5 18,14.5 10,19 2,14.5 2,5.5" fill="#f05a24"/></svg>Proven results that drive</div>
  <h2 class="head">Real Growth</h2>
  <p class="lead">We've helped brands strengthen their digital presence, expand their network, and accelerate opportunities across the defense, space, and government sectors, in just one year, our clients have achieved:</p>
  <div class="stat" style="left:90px"><strong>+72%</strong><p>Increase in database contacts through CRM implementation and targeted marketing campaigns</p></div>
  <div class="stat" style="left:440px"><strong>100+</strong><p>Introductions to tech-scouting contracts across the DoD and the aerospace &amp; defense ecosystem</p></div>
  <div class="stat-hex">
    <svg width="200" height="180" viewBox="0 0 200 180"><polygon points="50,2 150,2 198,90 150,178 50,178 2,90" fill="none" stroke="rgba(255,255,255,.35)" stroke-width="1.5"/><rect x="44" y="40" width="26" height="26" fill="none" stroke="#7cc242" stroke-width="2"/><polyline points="49,59 56,52 61,56 66,47" fill="none" stroke="#7cc242" stroke-width="2"/></svg>
    <p>Positioned a client for transformative growth, fueling a 570% increase in stock price and attracting $50M in new investment</p>
  </div>
</section>

<section class="testimonial">
  <svg class="quote-mark" width="46" height="40" viewBox="0 0 46 40"><path d="M0 40V20C0 8 6 2 18 0v8c-6 2-8 6-8 12h8v20zM26 40V20C26 8 32 2 44 0v8c-6 2-8 6-8 12h8v20z" fill="#2b8fe0"/></svg>
  <p class="quote">Partnering with Harrowfield Bright Associates accelerated the growth of our company. Their strategic insight, deep federal expertise, and hands-on support transformed our U.S. expansion. In less than six months, they built our presence in the United States from the ground up, helping us secure contracts, advocates, and visibility at the highest levels. Working with Harrowfield Bright Associates has been a true game changer for our company.</p>
  <div class="quote-name head">Martin Calloway</div>
  <div class="quote-role">President &amp; Managing Director, Ironvale Metals USA</div>
  <svg class="quote-nav" width="60" height="26" viewBox="0 0 60 26"><polygon points="13,1 24,7 24,19 13,25 2,19 2,7" fill="none" stroke="#f05a24"/><polyline points="15,9 11,13 15,17" fill="none" stroke="#f05a24" stroke-width="1.5"/><polygon points="45,1 56,7 56,19 45,25 34,19 34,7" fill="none" stroke="#f05a24"/><polyline points="43,9 47,13 43,17" fill="none" stroke="#f05a24" stroke-width="1.5"/></svg>
  <div class="portrait" role="img" aria-label="Portrait photo of Martin Calloway with coloured triangle accents"></div>
</section>

<section class="edge">
  <div class="edge-photo" role="img" aria-label="Aerial photo of offshore oil rigs over deep blue water"></div>
  <h2 class="head">Our Edge</h2>
  <p>We combine deep federal sector insight, technical understanding, and a powerful network across government, industry, investors, and media. Our proven approach drives results — from clear contract wins and successful bids to increased valuation, strategic investments, and political support. Our strategies begin with your mission and scale growth, ensuring every message, relationship, and action advances growth and impact.</p>
</section>

<section class="partner">
  <div class="eyebrow head"><svg width="16" height="16" viewBox="0 0 20 20"><polygon points="10,1 18,5.5 18,14.5 10,19 2,14.5 2,5.5" fill="#2b8fe0"/></svg>What to expect when</div>
  <h2 class="head">Partnering With Us</h2>
  <p class="lead">With decades of experience, a results-focused methodology, and cutting-edge marketing and communications tools and technologies, we begin every engagement with a discovery and planning process to ensure we are building a strategy that cuts through the noise to achieve our measurable results. As specialists in government crisis communications, we additionally examine our client's current strategy for risks ensuring we are building on a stable foundation.</p>
  <div class="wheel" role="img" aria-label="Circular service diagram with the brand at its centre and service areas around it"></div>
  <div class="partner-copy">
    <p>By truly understanding our client's goals, key milestones, potential areas of risk, ideal customer and investor targets, position profiles, and what key drivers, we create messaging and a strategy that goes beyond traditional brand awareness to meet mission objectives. As a full-service firm, we work across all the areas in the graphic.</p>
    <p>Our time-tested methodology is based on building and executing a strategy aligned with client mission objectives. With the strategy in place, we execute tactics with precision, efficiency, and the highest quality of customer service.</p>
    <span class="btn">GET IN TOUCH</span>
  </div>
</section>

<footer class="footer">
  <div class="subscribe head">Subscribe<span>To Our Newsletter</span></div>
  <div class="email-field"><span>email@example.com</span><span>&#10148;</span></div>
  <div class="foot-col" style="left:650px">
    <h4>Navigation</h4>
    <div>Home</div><div>Advisory Services</div><div>About Us</div><div>Blog</div><div>Contact Us</div>
  </div>
  <div class="foot-col contact" style="left:870px">
    <h4>Contact</h4>
    <div class="contact-row"><i></i><div>info@harrowfieldbright.com</div></div>
    <div class="contact-row"><i></i><div>Meridian Works<br>Harrowfield Bright Associates<br>418 Alder St<br>Suite 210<br>Austin, TX 78701</div></div>
  </div>
  <div class="copyright">© COPYRIGHT HARROWFIELD BRIGHT 2025. ALL RIGHTS RESERVED.</div>
</footer>

</body>
</html>
```